Create a 3-4 page concept for an electrical contracting company

We are a company that requires a new look for our website. We are familiar with Wordpress to be able to update using any theme or builder supplied.

While typical ideas of construction may get the yellow and blue colour pallette, hard hats, hammers, or lightning bolts entering the arena, we are completely against this image.

We intend for the website to have instant appeal and intuitive navigation. The home page should have a creative use of angles or brand identification with the banner or menubar if needed.

After combing hundreds of wordpress templates, the most attractive seem to be aimed at beauty services. Unfortunately we do not have a lot of picture perfect material to showcase, but it can be blended in other ways. - the brand should be recognizable and captivating.

Target Market(s)

High-end contracting firms focused on quality and service for long term projects (Custom Homes)

Industry/Entity Type

Contracting

Font styles to use
Sans Serif
Other font styles liked:
• Gotham usually. Adjusted kerning and rounded edges seem to be more friendly

Requirements
Must have
• Creative use of the logo shape and colour scheme, especially at the home.

Use of a CMS to be modifiable from a browser (Wordpress,etc) - A builder such as muffin, divi, or elementor accepted!

Elements or sections that could be adaptable for use. About us, members, contact, services... etc. Content would be written after
Nice to have
• Some clean inspiration that we appreciate:

www.brindlework.ca
www.harrowfieldbuilders.com
Should not have
• Generic welcome banner...

```html
<!DOCTYPE html>
<html lang="en">
<head>
<meta charset="utf-8">
<title>Northvale Electric — Who We Are</title>
<link href="https://fonts.googleapis.com/css2?family=Fira+Sans:wght@500;600;700&family=Lato:wght@300;400&display=swap" rel="stylesheet">
<style>
:root{
  --slate:#34465c;
  --slate-deep:#243243;
  --footer:#3e5268;
  --ink:#1f2630;
  --muted:#7c8591;
  --teal:#5ec8c8;
  --copper:#d9822b;
  --paper:#ffffff;
  --mist:#f4f5f7;
}
*{box-sizing:border-box;margin:0;padding:0}
html,body{width:1200px;height:4273px;overflow:hidden;background:var(--paper)}
body{position:relative;font-family:"Lato",sans-serif;color:var(--ink)}
.abs{position:absolute}
h1,h2,h3,.brand,.btn{font-family:"Fira Sans",sans-serif}

.hero{left:0;top:0;width:1200px;height:622px;background:linear-gradient(120deg,#263548 0%,#44607a 45%,#2e4259 75%,#4a6278 100%)}
.brand{display:flex;align-items:center;gap:12px;color:#fff;font-weight:600;font-size:21px;line-height:1;letter-spacing:1px}
.brand .mark{width:34px;height:34px;background:#fff}
.brand small{display:block;font-size:18px;font-weight:500;letter-spacing:2px}
.lang{left:780px;top:52px;color:#fff;font-size:13px;display:flex;gap:8px;align-items:center}
.lang i{display:inline-block;width:14px;height:9px;background:#c9d3e6}
.btn-touch{left:858px;top:38px;width:168px;height:43px;border:1.5px solid var(--copper);color:var(--copper);font-size:13px;font-weight:600;display:flex;align-items:center;justify-content:center;letter-spacing:.3px}
.burger{left:1054px;top:48px;width:32px}
.burger span{display:block;height:3px;background:#fff;margin-bottom:7px}
.hero-title{left:0;top:258px;width:1200px;text-align:center;color:#fff;font-size:62px;font-weight:700;letter-spacing:1px}

.intro{left:110px;top:525px;width:977px;height:192px;background:#fff;box-shadow:0 10px 30px rgba(30,40,60,.12);border-radius:4px}
.intro p{position:absolute;left:56px;top:50px;width:560px;font-size:18px;line-height:31.5px;font-weight:300;color:var(--muted)}
.intro .rule{position:absolute;left:648px;top:46px;width:2px;height:100px;background:#2b3440}
.intro h2{position:absolute;left:697px;top:56px;font-size:33px;line-height:43px;font-weight:600;color:#263245}

.values-title{left:0;top:835px;width:942px;text-align:center;font-size:42px;font-weight:600;color:#202833}
.value{width:240px}
.value svg{position:absolute;left:0;top:0}
.value h3{position:absolute;font-size:27px;line-height:31px;font-weight:500;color:#232b36}
.value p{position:absolute;font-size:18px;line-height:31.5px;font-weight:300;color:var(--muted);width:225px}
.values-photo{left:837px;top:830px;width:363px;height:651px;background:linear-gradient(150deg,#d6dcda 0%,#99aaa9 40%,#4c6a72 80%,#2a4451 100%)}

.story{left:0;top:1632px;width:1200px;height:700px;background:linear-gradient(100deg,#2b3138 0%,#4b535c 40%,#6a727a 65%,#3d444c 100%)}
.story h2{position:absolute;left:110px;top:108px;color:#fff;font-size:42px;font-weight:600}
.story .copy{position:absolute;left:696px;top:106px;width:352px;color:#fff;font-size:18px;line-height:31.6px;font-weight:300}
.story .copy p+p{margin-top:31.6px}

.team{left:111px;top:2490px;width:976px;height:533px;background:linear-gradient(180deg,#e0e5e8 0%,#aeb8bf 45%,#545e69 100%)}
.slide-nav{left:916px;top:2966px;width:171px;height:57px;display:flex}
.slide-nav div{flex:1;display:flex;align-items:center;justify-content:center}
.slide-nav .prev{background:var(--slate)}
.slide-nav .next{background:#fff}

.contact{left:0;top:3151px;width:1200px;height:833px;background:var(--mist)}
.contact-title{left:110px;top:3330px;font-size:42px;line-height:53px;font-weight:600;color:#232b36}
.contact-rule{left:110px;top:3461px;width:136px;height:2px;background:#232b36}
.contact-lead{left:110px;top:3494px;width:330px;font-size:18px;line-height:27px;font-weight:300;color:var(--muted)}
.form{left:551px;top:3283px;width:475px;height:548px;background:#fff;box-shadow:0 10px 30px rgba(30,40,60,.08)}
.field{position:absolute;left:65px;width:334px;border-bottom:1.5px solid var(--teal);height:36px;display:flex;align-items:center;gap:14px;padding-left:10px;font-size:12px;color:#9aa2ac}
.field svg{flex:none}
.send{position:absolute;left:65px;top:440px;width:331px;height:50px;background:var(--copper);color:#fff;font-family:"Fira Sans",sans-serif;font-size:16px;font-weight:600;display:flex;align-items:center;justify-content:center}

.footer{left:0;top:3984px;width:1200px;height:289px;background:var(--footer);color:#fff}
.footer .brand{position:absolute;left:111px;top:108px;font-size:26px}
.footer .brand small{font-size:22px}
.footer .brand .mark{width:40px;height:40px}
.footer .copy{position:absolute;left:111px;top:170px;font-size:15px;line-height:27px;font-weight:300}
.footer .addr{position:absolute;left:420px;top:82px;font-size:15px;line-height:28px;font-weight:300}
.footer .links{position:absolute;left:755px;top:82px;font-size:15px;line-height:27px;font-weight:300;list-style:none}
.footer .social{position:absolute;left:922px;top:88px;display:flex;gap:30px}
.footer .social span{width:18px;height:18px;border-radius:50%;background:#fff}
</style>
</head>
<body>

<section class="abs hero" role="img" aria-label="Photo of an electrician checking a control panel with a tablet, tinted slate"></section>
<div class="abs brand" style="left:111px;top:36px"><span class="mark"></span><span>NORTHVALE<small>ELECTRIC</small></span></div>
<div class="abs lang">EN <i></i> <svg width="8" height="6" viewBox="0 0 8 6"><path d="M1 1l3 3 3-3" stroke="#fff" fill="none"/></svg></div>
<a class="abs btn btn-touch">GET IN TOUCH</a>
<div class="abs burger"><span></span><span></span><span></span></div>
<h1 class="abs hero-title">WHO WE ARE</h1>

<div class="abs intro">
  <p>Pellentesque at tincidunt lorem, sollicitudin eleifend ante. Nunc vestibulum facilisis leo. Mauris iaculis suscipit ligula, nec luctus ligula pulvinar in.</p>
  <span class="rule"></span>
  <h2>BUILD WITH<br>INTEGRITY</h2>
</div>

<h2 class="abs values-title">OUR VALUES</h2>

<div class="abs value" style="left:116px;top:955px">
  <svg width="70" height="70" viewBox="0 0 70 70" fill="none" stroke="#34465c" stroke-width="2.5"><path d="M12 58V38h8v-8M34 18c-8 0-14 6-14 14v6M52 8c-10 0-18 8-18 18v20h16"/><rect x="34" y="32" width="16" height="20" rx="3"/><circle cx="42" cy="42" r="3"/></svg>
  <h3 style="left:98px;top:0">Electricity<br>for life</h3>
  <p style="left:98px;top:84px">Pellentesque at tincidunt lorem, sollicitudin eleifend ante. Nunc vestibulum facilisis leo.</p>
</div>
<div class="abs value" style="left:458px;top:955px">
  <svg width="66" height="66" viewBox="0 0 66 66" fill="none" stroke="#34465c" stroke-width="2.5"><circle cx="33" cy="33" r="30"/><path d="M27 18v8M39 18v8M22 26h22v8a11 11 0 0 1-22 0zM33 45v8"/></svg>
  <h3 style="left:93px;top:0">Electricity<br>for life</h3>
  <p style="left:93px;top:84px">Pellentesque at tincidunt lorem, sollicitudin eleifend ante. Nunc vestibulum facilisis leo.</p>
</div>
<div class="abs value" style="left:116px;top:1242px">
  <svg width="66" height="66" viewBox="0 0 66 66" fill="none" stroke="#34465c" stroke-width="2.5"><path d="M18 10A28 28 0 0 0 33 62M48 10A28 28 0 0 1 33 62"/><rect x="22" y="20" width="22" height="18" rx="3"/><path d="M27 12v8M39 12v8M33 38v10M28 29h10"/></svg>
  <h3 style="left:95px;top:0">Electricity<br>for life</h3>
  <p style="left:95px;top:84px">Pellentesque at tincidunt lorem, sollicitudin eleifend ante. Nunc vestibulum facilisis leo.</p>
</div>
<div class="abs value" style="left:458px;top:1240px">
  <svg width="66" height="66" viewBox="0 0 66 66" fill="none" stroke="#34465c" stroke-width="2.2"><circle cx="8" cy="6" r="3"/><circle cx="22" cy="6" r="3"/><circle cx="44" cy="6" r="3"/><circle cx="58" cy="6" r="3"/><path d="M8 9v14l14 12M22 9v26M44 9v26M58 9v14L44 35M4 42h58M4 50h58M4 58h58M33 35v7"/></svg>
  <h3 style="left:90px;top:0">Electricity<br>for life</h3>
  <p style="left:90px;top:86px">Pellentesque at tincidunt lorem, sollicitudin eleifend ante. Nunc vestibulum facilisis leo.</p>
</div>
<div class="abs values-photo" role="img" aria-label="Photo of two colleagues smiling while looking at a laptop"></div>

<section class="abs story">
  <div role="img" aria-label="Black and white photo of workers among industrial fan machinery" style="position:absolute;inset:0"></div>
  <h2>OUR STORY</h2>
  <div class="copy">
    <p>Nulla mattis nisi ullamcorper dignissim euismod. Nam ultrices sit amet lectus quis vulputate. Proin rhoncus, felis ut ullamcorper sagittis, ipsum nunc rutrum mauris, malesuada laoreet purus quam sed nisi. Morbi rutrum tortor a sapien vulputate, ornare imperdiet justo congue.</p>
    <p>Nulla mattis nisi ullamcorper dignissim euismod. Nam ultrices sit amet lectus quis vulputate. Proin rhoncus, felis ut ullamcorper sagittis, ipsum nunc rutrum mauris, malesuada laoreet purus quam sed nisi. Morbi rutrum tortor a sapien vulputate, ornare imperdiet justo congue.</p>
  </div>
</section>

<div class="abs team" role="img" aria-label="Photo of the team standing together in a bright office"></div>
<div class="abs slide-nav">
  <div class="prev"><svg width="12" height="20" viewBox="0 0 12 20"><path d="M10 2L2 10l8 8" stroke="#fff" stroke-width="2.5" fill="none"/></svg></div>
  <div class="next"><svg width="12" height="20" viewBox="0 0 12 20"><path d="M2 2l8 8-8 8" stroke="#34465c" stroke-width="2.5" fill="none"/></svg></div>
</div>

<section class="abs contact">
  <svg width="1200" height="833" viewBox="0 0 1200 833" style="position:absolute;left:0;top:0" fill="none" stroke="#e4e8ee" stroke-width="2">
    <path d="M880 40l140-80 140 80v160l-140 80-140-80z"/><path d="M1020 120l140 80v160"/>
    <path d="M-20 560l160-90 180 100v200"/><path d="M60 620l160 90v120"/>
  </svg>
</section>
<h2 class="abs contact-title">GET IN<br>TOUCH</h2>
<span class="abs contact-rule"></span>
<p class="abs contact-lead">Proin rhoncus, felis ut ullamcorper sagittis, ipsum nunc rutrum mauris, malesuada laoreet purus quam sed nisi.</p>

<form class="abs form">
  <div class="field" style="top:46px"><svg width="12" height="12" viewBox="0 0 12 12" fill="none" stroke="#8a929c"><circle cx="6" cy="4" r="2.5"/><path d="M1.5 11.5c0-3 9-3 9 0"/></svg>Name</div>
  <div class="field" style="top:106px"><svg width="12" height="12" viewBox="0 0 12 12" fill="none" stroke="#8a929c"><rect x="2.5" y="1.5" width="7" height="10"/></svg>Company Name</div>
  <div class="field" style="top:167px"><svg width="12" height="12" viewBox="0 0 12 12" fill="none" stroke="#8a929c"><rect x="1" y="2.5" width="10" height="7"/><path d="M1 2.5l5 4 5-4"/></svg>Email Address</div>
  <div class="field" style="top:228px"><svg width="12" height="12" viewBox="0 0 12 12" fill="none" stroke="#8a929c"><circle cx="6" cy="6" r="5"/><path d="M4 4l1 2 2 1"/></svg>Phone Number</div>
  <div class="field" style="top:290px;height:106px;align-items:flex-start;padding-top:12px"><svg width="12" height="12" viewBox="0 0 12 12" fill="none" stroke="#8a929c"><rect x="1" y="2" width="10" height="7"/><path d="M3 5h6"/></svg>Messages</div>
  <div class="send">SEND!</div>
</form>

<footer class="abs footer">
  <div class="brand"><span class="mark"></span><span>NORTHVALE<small>ELECTRIC</small></span></div>
  <p class="copy">© 2020. Northvale Electric Company.<br>Alright Reserve.</p>
  <p class="addr">Linden Row 88, Austin, US<br>p. (+1) 555 0142<br>e. hello@northvaleelectric.com</p>
  <ul class="links"><li>About Us</li><li>Members</li><li>Contact</li><li>Services</li></ul>
  <div class="social" aria-label="Social links"><span></span><span></span><span></span><span></span></div>
</footer>

</body>
</html>
```